Wren Hollow Apartments
stationary
Wren Hollow Apartments - Real Estate
Creative Brief
Traditional
Tobias Lindqvist
2408 Wren Hollow Houston TX 77091
tjlindqvist@quellmail.example

```html
<!DOCTYPE html>
<html lang="en">
<head>
<meta charset="utf-8">
<title>Wren Hollow Apartments — Business Card</title>
<link rel="stylesheet" href="https://fonts.googleapis.com/css2?family=Libre+Baskerville&display=swap">
<style>
  :root {
    --page-bg: #e4e6e4;
    --card-white: #ffffff;
    --brand-green: #2f8a3c;
    --band-black: #111111;
    --ink: #2a2a2a;
    --name-white: #ffffff;
  }
  * { margin: 0; padding: 0; box-sizing: border-box; }
  html, body {
    width: 1200px; height: 1009px; overflow: hidden;
    background: var(--page-bg);
    font-family: "Libre Baskerville", "Times New Roman", serif;
  }
  .sheet {
    width: 1200px; height: 1009px;
    display: flex; flex-direction: column; align-items: center; justify-content: center;
    gap: 40px;
  }
  .card {
    position: relative;
    width: 800px; height: 457px;
    background: var(--card-white);
    border-radius: 26px;
    overflow: hidden;
    box-shadow: 0 4px 14px rgba(0,0,0,0.12);
  }
  .card-back { display: flex; align-items: center; justify-content: center; }
  .brand {
    display: flex; align-items: center; gap: 16px;
    color: var(--brand-green);
    font-weight: 400;
    letter-spacing: 0.04em;
  }
  .brand-mark { width: 38px; height: 38px; background: var(--brand-green); border-radius: 4px; flex: none; }
  .card-back .brand-name { font-size: 40px; }
  .card-front .brand { position: absolute; left: 44px; top: 52px; }
  .card-front .brand-mark { width: 26px; height: 26px; }
  .card-front .brand-name { font-size: 24px; }
  .front-art { position: absolute; inset: 0; }
  .contact {
    position: absolute; left: 92px; top: 122px;
    list-style: none;
    color: var(--ink);
    font-size: 15px; line-height: 1.6;
  }
  .contact li { display: flex; align-items: center; gap: 8px; }
  .contact .no-icon { padding-left: 22px; }
  .contact svg { width: 14px; height: 14px; flex: none; }
  .holder-name {
    position: absolute; right: 70px; bottom: 40px;
    color: var(--name-white);
    font-size: 24px; letter-spacing: 0.06em; text-transform: uppercase;
  }
</style>
</head>
<body>
<main class="sheet">
  <section class="card card-back">
    <div class="brand">
      <span class="brand-mark"></span>
      <span class="brand-name">Wren Hollow Apartments</span>
    </div>
  </section>

  <section class="card card-front">
    <svg class="front-art" viewBox="0 0 800 457" preserveAspectRatio="none" aria-hidden="true">
      <path d="M0,300 C260,312 520,290 800,165 L800,457 L0,457 Z" fill="var(--band-black)"/>
      <path d="M0,330 C300,342 560,326 800,255 L800,457 L0,457 Z" fill="var(--brand-green)"/>
    </svg>

    <div class="brand">
      <span class="brand-mark"></span>
      <span class="brand-name">Wren Hollow Apartments</span>
    </div>

    <ul class="contact">
      <li class="no-icon">2408 Wren Hollow</li>
      <li class="no-icon">Houston TX 77091</li>
      <li>
        <svg viewBox="0 0 14 14"><path d="M3,1 L5.5,1 L6.5,4 L5,5.2 C5.8,7 7,8.2 8.8,9 L10,7.5 L13,8.5 L13,11 C13,12 12,13 11,13 C5.5,12.6 1.4,8.5 1,3 C1,2 2,1 3,1 Z" fill="var(--brand-green)"/></svg>
        713-555-0148
      </li>
      <li>
        <svg viewBox="0 0 14 14"><rect x="1" y="3" width="12" height="8" rx="1" fill="var(--brand-green)"/><path d="M1.5,3.5 L7,8 L12.5,3.5" stroke="#fff" stroke-width="1" fill="none"/></svg>
        tjlindqvist@quellmail.example
      </li>
    </ul>

    <p class="holder-name">Tobias Lindqvist</p>
  </section>
</main>
</body>
</html>
```